deceased estate clean ups brochures

we would like a brochure to reresent our business we already have new web site and want to do DL A4 brochure to give out to promote our business we already have logo www.larkmore.com.au is where you can get all info needed

Target Market(s)

families with loved ones that have past away
people done sizing or needing to decluter

Colors
cadf82
33b8a4
886aae
33a6d7

```html
<!DOCTYPE html>
<html lang="en">
<head>
<meta charset="utf-8">
<title>Larkmore – Deceased Estate Cleanups Brochure</title>
<link href="https://fonts.googleapis.com/css2?family=Open+Sans:wght@300;400;600;700&family=Ubuntu:wght@500;700&display=swap" rel="stylesheet">
<style>
:root{
  --lime:#cadf82;
  --teal:#33b8a4;
  --purple:#886aae;
  --blue:#33a6d7;
  --ink:#2b2b2b;
  --body:#4a4a4a;
  --paper:#f8f8f8;
  --canvas:#e6e7e9;
}
*{box-sizing:border-box;margin:0;padding:0}
html,body{width:1149px;height:1200px;overflow:hidden;background:var(--canvas)}
body{font-family:"Open Sans",Arial,sans-serif;color:var(--body);position:relative}
.brochure{position:absolute;left:34px;top:214px;width:1080px;height:772px;display:flex;box-shadow:0 10px 30px rgba(0,0,0,.12)}
.panel{position:relative;width:360px;height:772px;background:var(--paper);overflow:hidden}
.band-top{position:absolute;left:0;top:0;height:32px}
.band-bottom{position:absolute;left:0;bottom:0;height:32px;width:100%;display:flex;align-items:center}
.url{font-family:"Ubuntu",sans-serif;font-weight:700;font-size:13.5px;color:#fff;padding-left:12px;letter-spacing:.2px}
.heading{font-family:"Ubuntu",sans-serif;font-weight:700;color:var(--ink);text-transform:uppercase}
.photo{position:absolute}
p{font-weight:300;font-size:11.4px;line-height:15.4px}
b{font-weight:700;color:var(--ink)}

/* about panel */
.about .band-top{width:100%;background:var(--lime)}
.about .heading{position:absolute;left:12px;top:44px;font-size:17.5px}
.about .photo-grief{left:0;top:72px;width:178px;height:178px;background:linear-gradient(135deg,#8c8479,#b49876 60%,#6d6259)}
.about .photo-couple{left:178px;top:72px;width:182px;height:178px;background:linear-gradient(135deg,#cfc6b8,#e7dfd3 55%,#b9a590)}
.about .rule{position:absolute;left:0;top:276px;width:9px;height:392px;background:var(--blue)}
.about .copy{position:absolute;left:70px;top:274px;width:282px}
.about .copy p+p{margin-top:9px}
.about .band-bottom{background:var(--blue)}

/* why panel */
.why .band-top{width:100%;background:var(--purple)}
.why .intro{position:absolute;left:28px;top:40px;font-size:17.5px}
.why .section{position:absolute;left:28px;width:228px}
.why .section .heading{font-size:14.5px;margin-bottom:13px}
.why .thumb{position:absolute;right:8px;width:94px;height:98px}
.why .areas p{font-size:10.8px;line-height:14px}
.why .contact{position:absolute;left:28px;top:638px;width:320px}
.why .contact .heading{font-size:17px}
.why .contact-row{display:flex;align-items:flex-start;margin-top:6px}
.brand-mark{display:flex;flex-direction:column;align-items:center;width:100px;margin-top:14px}
.brand-mark .dot{width:26px;height:26px;border-radius:50%;background:var(--lime);margin-bottom:6px}
.brand-mark .name{font-family:"Ubuntu",sans-serif;font-weight:500;font-size:14px;color:var(--ink);letter-spacing:1.5px}
.details{list-style:none;font-family:"Ubuntu",sans-serif;font-weight:700;font-size:11.4px;color:var(--ink);line-height:14.2px;margin-left:6px}
.details li{display:flex;align-items:center;gap:4px}
.details svg{width:9px;height:9px;flex:none}
.why .band-bottom{background:var(--lime)}

/* cover panel */
.cover .band-top{width:172px;background:var(--teal)}
.cover .logo{position:absolute;right:30px;top:58px;display:flex;flex-direction:column;align-items:center}
.cover .logo .dot{width:54px;height:54px;border-radius:50%;background:var(--lime);margin-bottom:12px}
.cover .logo .name{font-family:"Ubuntu",sans-serif;font-weight:500;font-size:22px;letter-spacing:2.5px;color:var(--ink)}
.cover .photo-note{left:0;top:222px;width:360px;height:154px;background:linear-gradient(100deg,#c9b98a,#e6dcc3 35%,#8ea6bd 70%,#5f86a8)}
.cover .tagline{position:absolute;left:86px;top:484px;width:250px}
.cover .tagline h2{font-family:"Ubuntu",sans-serif;font-weight:700;font-size:15px;line-height:18px;color:var(--ink)}
.cover .tagline p{font-weight:400;font-size:13.6px;line-height:19px;margin-top:16px}
.cover .band-bottom{background:var(--teal)}
.cover .band-bottom .accent{position:absolute;right:0;top:0;width:90px;height:32px;background:var(--purple)}
</style>
</head>
<body>
<main class="brochure">

  <section class="panel about">
    <div class="band-top"></div>
    <h2 class="heading">About our company</h2>
    <div class="photo photo-grief" role="img" aria-label="Photo of a woman with her head in her hands beside a moving box"></div>
    <div class="photo photo-couple" role="img" aria-label="Photo of a smiling older couple reviewing papers"></div>
    <div class="rule"></div>
    <div class="copy">
      <p>At <b>Larkmore</b> our goal is to ease your worries and help you with your journey in preparing your house for rental or resale.</p>
      <p>Whether it is a move to another residence or the difficult task with dealing with the grief when a loved one passes away, <b>Larkmore</b> can help with the preparation of the property for sale. <b>Larkmore</b> will come in, remove unwanted items and dispose of all rubbish, do cosmetic repairs if required and leave the property in a spotless state.<br>Our trained and reliable staff, repair any house and carry out landscaping in preparation for renting or resale of the property in a timely and professional manner. Our team provides a discrete and trustworthy service, keeping in mind the sensitive nature of the work.</p>
      <p><b>Larkmore</b> will make sure that all remaining furniture and possessions left inside the property are removed/sold/taken to storage and the remainder of unwanted goods are sorted so that the entire property is completely cleared for rental or sale.</p>
    </div>
    <div class="band-bottom"><span class="url">www.larkmore.com.au</span></div>
  </section>

  <section class="panel why">
    <div class="band-top"></div>
    <h2 class="heading intro">Why choose us</h2>

    <div class="section" style="top:62px">
      <h3 class="heading">Quality</h3>
      <p>Our goal is to enhance your property and achieve the results you are looking for. We appreciate the trust placed in us to deliver a quality job that meets your expectations.</p>
    </div>
    <div class="thumb" style="top:64px;background:linear-gradient(135deg,#9fb6c8,#3e6f9e)" role="img" aria-label="Photo of two removalists with a clipboard"></div>

    <div class="section" style="top:174px">
      <h3 class="heading">Pride</h3>
      <p>We take pride in our family approach and care we bring to your loved ones belongings. Whether it is simple house clearing, house repairs or larger renovations your home will be ready for rental or sale.</p>
    </div>
    <div class="thumb" style="top:176px;background:linear-gradient(135deg,#d9d3c9,#8f959b)" role="img" aria-label="Photo of an older couple at a laptop"></div>

    <div class="section" style="top:286px">
      <h3 class="heading">Professionalism</h3>
      <p>Larkmore only use quality staff and materials that are “fit for purpose”.<br>We keep a professional approach to every job ensuring all agreed tasks are completed and accounted for.</p>
    </div>
    <div class="thumb" style="top:288px;background:linear-gradient(135deg,#c8b08c,#2f5d95)" role="img" aria-label="Photo of a removalist carrying a box"></div>

    <div class="section areas" style="top:398px">
      <h3 class="heading">Areas serviced</h3>
      <p>Specialising in Melbourne CBD and suburbs including:<br>Coburg, Falkner, Campbellfield, Craigieburn, St. Kilda, Brighton, Caulfield, Hawthorn, Heidelberg, Watsonia<br>Richmond, Carlton, Collingwood, Brunswick South Melbourne, Williamstown, Footscray, Newport, Altona, Sunshine<br>Essendon, Avondale Heights, St. Albans, Keilor, Taylors Lakes, Sydenham<br>Diggers Rest, Sunbury, Gisborne</p>
      <p style="margin-top:12px">If you’re not sure we service your area, give us a call.</p>
    </div>
    <div class="thumb" style="top:400px;background:linear-gradient(135deg,#b8bec6,#485d78)" role="img" aria-label="Photo of removalists loading wrapped furniture into a van"></div>

    <div class="contact">
      <h2 class="heading">Contact us</h2>
      <div class="contact-row">
        <div class="brand-mark"><span class="dot"></span><span class="name">LARKMORE</span></div>
        <ul class="details">
          <li><svg viewBox="0 0 10 10"><rect x="1" y="1" width="8" height="8" fill="none" stroke="#2b2b2b" stroke-width="1.6"/></svg>PO Box 208, Kelsey 3190</li>
          <li><svg viewBox="0 0 10 10"><path d="M2 1l2 2-1 1.5c.8 1.4 1.6 2.2 3 3L7.5 6l2 2-1.5 1.5C4.5 9 1 5.5.5 2.5z" fill="#2b2b2b"/></svg>0400 318 624</li>
          <li><svg viewBox="0 0 10 10"><rect x="2.5" y="0.5" width="5" height="9" rx="1" fill="#2b2b2b"/></svg>0400 318 624</li>
          <li><svg viewBox="0 0 10 10"><rect x="0.5" y="2" width="9" height="6.5" fill="#2b2b2b"/><path d="M.5 2l4.5 3.5L9.5 2" stroke="#fff" fill="none"/></svg>info@larkmore.com.au</li>
          <li><svg viewBox="0 0 10 10"><circle cx="5" cy="5" r="4.2" fill="none" stroke="#2b2b2b" stroke-width="1.2"/><path d="M1 5h8M5 1c-2 2.5-2 5.5 0 8M5 1c2 2.5 2 5.5 0 8" stroke="#2b2b2b" fill="none" stroke-width=".8"/></svg>www.larkmore.com.au</li>
        </ul>
      </div>
    </div>
    <div class="band-bottom"></div>
  </section>

  <section class="panel cover">
    <div class="band-top"></div>
    <div class="logo"><span class="dot"></span><span class="name">LARKMORE</span></div>
    <div class="photo photo-note" role="img" aria-label="Photo of a handwritten note reading keep, recycle, declutter, trash, sell, donate beside a mug on a blue wooden table"></div>
    <div class="tagline">
      <h2>We’re here to help<br>Deceased Estate Cleanups</h2>
      <p>At Larkmore our goal is to ease your worries and help you with your journey in preparing your house for rental or resale.</p>
    </div>
    <div class="band-bottom"><span class="url">www.larkmore.com.au</span><span class="accent"></span></div>
  </section>

</main>
</body>
</html>
```